New Business Tri Fold Brochure

Tri Fold Brochure for new business. I have attached a few versions of our logo and would like the color scheme to be the blue and grey colors from the logo. I have also attached examples of the data that I would like implemented into the brochure such as the FAQ's and general company information. I would like the 3 general points (hassle free, save money, no risk guarantee) to be matched to appropriate icons. I also need the 3 steps for "how it works" matched to appropriate themed icons. I would like the back of the brochure to have a photo of our building, map of location and all contact information. Address: 718 W. Corbin Ridge Ave Suite 200 Fort Lauderdale FL 33309. Phone- 754-618-2907. Email: info@tallowbrook-ledger.com. Website: www.tallowbrook-ledger.com

```html
<!DOCTYPE html>
<html lang="en">
<head>
<meta charset="utf-8">
<title>Tallowbrook Ledger – Tri Fold Brochure</title>
<link href="https://fonts.googleapis.com/css2?family=Open+Sans:ital,wght@0,400;0,600;0,700;0,800;1,400;1,800&display=swap" rel="stylesheet">
<style>
  :root{
    --brand-blue:#2b72b9;
    --brand-blue-deep:#1f5f9f;
    --brand-grey:#7b7c7e;
    --ink:#4f5256;
    --paper:#ffffff;
    --backdrop:#e4e5e6;
  }
  *{box-sizing:border-box;margin:0;padding:0}
  html,body{width:759px;height:1200px;overflow:hidden;background:var(--backdrop);font-family:"Open Sans",Arial,sans-serif;color:var(--ink)}
  .canvas{position:relative;width:759px;height:1200px}
  .spread{position:absolute;left:20px;width:719px;height:556px;overflow:hidden;background:var(--brand-blue);box-shadow:0 6px 18px rgba(0,0,0,.18)}
  .spread--outside{top:20px}
  .spread--inside{top:624px}
  .shapes,.photo{position:absolute;left:0;top:0}
  .fold{position:absolute;top:0;width:1px;height:556px;background:rgba(0,0,0,.10)}
  .abs{position:absolute}

  .section-title{font-weight:800;font-style:italic;color:var(--brand-blue);font-size:15px;letter-spacing:-.2px;border-top:2px solid var(--brand-blue);display:inline-block;padding-top:1px}
  .body-copy{font-size:7.4px;line-height:1.45;font-style:italic;color:var(--ink)}

  .contact-label{color:var(--paper);font-weight:700;font-size:10px;letter-spacing:3px;text-align:center;width:239px}
  .contact-phone{color:var(--paper);font-weight:800;font-size:19px;text-align:center;width:239px}
  .contact-email{color:var(--paper);font-weight:600;font-size:9px;text-align:center;width:239px}
  .contact-address{color:var(--paper);font-size:7.6px;text-align:center;width:239px;line-height:1.4}
  .web{font-weight:700;font-size:9px;letter-spacing:.8px;text-align:center;width:240px}
  .web--light{color:var(--paper)}
  .web--blue{color:var(--brand-blue)}

  .brand{display:flex;align-items:center;gap:8px;justify-content:center;width:240px}
  .brand-dot{width:16px;height:16px;border-radius:50%;flex:none}
  .brand-name{font-weight:800;font-size:17px;line-height:1.05;text-transform:uppercase}
  .brand--blue .brand-name{color:var(--brand-blue)}
  .brand--blue .brand-dot{background:var(--brand-blue)}
  .brand--light .brand-name{color:var(--paper)}
  .brand--light .brand-dot{background:var(--paper)}

  .cover-title{font-weight:800;font-size:22px;line-height:1.02;text-align:center;width:240px;text-transform:uppercase}
  .cover-title .accent{color:var(--brand-blue)}
  .cover-title .muted{color:var(--brand-grey)}

  .benefit{position:absolute;left:24px;width:204px;display:flex;gap:8px}
  .benefit svg{flex:none}
  .benefit-title{font-weight:800;font-size:14px;text-transform:uppercase;line-height:1}
  .benefit-title .accent{color:var(--brand-blue)}
  .benefit-title .muted{color:var(--brand-grey)}
  .benefit-text{font-size:7.6px;line-height:1.35;margin-top:4px;color:var(--ink)}

  .tab{position:absolute;background:var(--brand-blue);color:var(--paper);font-weight:700;font-size:9px;letter-spacing:3.5px;padding:3px 10px}
  .tab--white{background:var(--paper);color:var(--brand-blue)}

  .step{position:absolute;left:258px;width:204px;display:flex;gap:8px}
  .step svg{flex:none}
  .step-title{font-weight:800;font-size:13px;color:var(--brand-blue);text-transform:uppercase;line-height:1}
  .step-text{font-size:7.4px;line-height:1.35;margin-top:3px;color:var(--ink)}

  .faq{position:absolute;left:496px;top:40px;width:208px;color:var(--paper)}
  .faq-q{font-weight:700;font-size:9px;line-height:1.2;margin-top:9px}
  .faq-a{font-size:6.6px;line-height:1.4;margin-top:2px;opacity:.95}
</style>
</head>
<body>
<div class="canvas">

  <!-- OUTSIDE SPREAD -->
  <section class="spread spread--outside" aria-label="Brochure outside">
    <svg class="shapes" width="719" height="556" viewBox="0 0 719 556" aria-hidden="true">
      <!-- back panel: grey band behind the text card -->
      <polygon points="16,250 224,250 224,336 16,372" fill="var(--brand-grey)"/>
      <path d="M16 16 H224 V292 H136 L120 312 L104 292 H16 Z" fill="var(--paper)"/>
      <!-- cover panel -->
      <rect x="479" y="0" width="240" height="556" fill="var(--paper)"/>
      <polygon points="479,170 719,150 719,430 479,410" fill="var(--brand-grey)"/>
      <circle cx="599" cy="290" r="104" fill="var(--brand-grey)"/>
      <path d="M479 410 Q599 380 719 410 V556 H479 Z" fill="var(--paper)"/>
    </svg>
    <svg class="photo" width="240" height="556" viewBox="0 0 240 556" role="img" aria-label="Photo of colleagues reviewing financial charts at a desk">
      <defs><linearGradient id="deskPhoto" x1="0" y1="0" x2="1" y2="1"><stop offset="0" stop-color="#6b4a35"/><stop offset=".55" stop-color="#d9dde3"/><stop offset="1" stop-color="#5b8cc4"/></linearGradient></defs>
      <path d="M0 400 Q120 360 240 392 V556 H0 Z" fill="url(#deskPhoto)"/>
    </svg>
    <svg class="photo" width="719" height="556" viewBox="0 0 719 556" role="img" aria-label="Photo of the office building with palm trees">
      <defs><linearGradient id="buildingPhoto" x1="0" y1="0" x2="0" y2="1"><stop offset="0" stop-color="#c9d6e2"/><stop offset=".4" stop-color="#8a6a4a"/><stop offset=".75" stop-color="#3e5a45"/><stop offset="1" stop-color="#6f8f5a"/></linearGradient></defs>
      <circle cx="599" cy="290" r="90" fill="url(#buildingPhoto)"/>
    </svg>
    <div class="fold" style="left:240px"></div>
    <div class="fold" style="left:479px"></div>

    <div class="abs" style="left:30px;top:28px;width:182px">
      <h2 class="section-title">WHO WE ARE</h2>
      <p class="body-copy" style="margin-top:6px">Tallowbrook Ledger is a company that was founded by previous merchant processing professionals with over 20 years of industry knowledge and experience. We know all of the tricks that the big companies use to fill their pockets with your money! We use that industry knowledge to negotiate and save your business money.</p>
      <h2 class="section-title" style="margin-top:12px">WHAT WE DO</h2>
      <p class="body-copy" style="margin-top:6px">Once you sign up, our experts get to work negotiating with your current merchant processing provider. Our goal is to get you the lowest rates possible without changing providers or having to get expensive new equipment. We offer a No Risk Savings Guarantee. If we can't save you money, you don't pay us a dime! 100% risk free.</p>
    </div>

    <p class="contact-label abs" style="left:240px;top:44px">CONTACT US</p>
    <p class="contact-phone abs" style="left:240px;top:64px">754-618-2907</p>
    <p class="contact-email abs" style="left:240px;top:92px">info@tallowbrook-ledger.com</p>
    <p class="contact-address abs" style="left:240px;top:112px">718 W. Corbin Ridge Ave Suite 200<br>Fort Lauderdale FL 33309</p>
    <div class="brand brand--light abs" style="left:240px;top:458px"><span class="brand-dot"></span><span class="brand-name">Tallowbrook<br>Ledger</span></div>
    <p class="web web--light abs" style="left:240px;top:518px">www.tallowbrook-ledger.com</p>

    <div class="brand brand--blue abs" style="left:479px;top:70px"><span class="brand-dot"></span><span class="brand-name">Tallowbrook<br>Ledger</span></div>
    <h1 class="cover-title abs" style="left:479px;top:440px"><span class="accent">Your<br>Business</span><br><span class="muted">Consultant</span></h1>
    <p class="web web--blue abs" style="left:479px;top:522px">www.tallowbrook-ledger.com</p>
  </section>

  <!-- INSIDE SPREAD -->
  <section class="spread spread--inside" aria-label="Brochure inside">
    <svg class="shapes" width="719" height="556" viewBox="0 0 719 556" aria-hidden="true">
      <rect x="16" y="0" width="463" height="556" fill="var(--paper)"/>
      <!-- left panel: grey band under photo -->
      <path d="M16 150 Q120 190 240 160 V220 Q120 250 16 210 Z" fill="var(--brand-grey)"/>
      <!-- centre panel: grey base band -->
      <polygon points="240,500 479,460 479,556 240,556" fill="var(--brand-grey)"/>
      <!-- right panel: grey band above photo -->
      <path d="M479 380 Q600 350 719 380 V556 H479 Z" fill="var(--brand-grey)"/>
    </svg>
    <svg class="photo" width="240" height="200" viewBox="0 0 240 200" role="img" aria-label="Photo of a businessman drawing a rising growth chart">
      <defs><linearGradient id="growthPhoto" x1="0" y1="0" x2="1" y2="1"><stop offset="0" stop-color="#cfd9e6"/><stop offset=".5" stop-color="#3d5d86"/><stop offset=".8" stop-color="#d9883e"/><stop offset="1" stop-color="#2b3f5c"/></linearGradient></defs>
      <path d="M0 0 H240 V140 Q120 170 0 130 Z" fill="url(#growthPhoto)"/>
    </svg>
    <svg class="photo" width="719" height="556" viewBox="0 0 719 556" role="img" aria-label="Photo of two business people shaking hands">
      <defs><linearGradient id="handshakePhoto" x1="0" y1="0" x2="1" y2="0"><stop offset="0" stop-color="#e7b06a"/><stop offset=".5" stop-color="#d99a7c"/><stop offset="1" stop-color="#c8ccd3"/></linearGradient></defs>
      <path d="M479 410 Q600 380 719 410 V556 H479 Z" fill="url(#handshakePhoto)"/>
    </svg>
    <div class="fold" style="left:240px"></div>
    <div class="fold" style="left:479px"></div>

    <div class="benefit" style="top:300px">
      <svg width="30" height="30" viewBox="0 0 30 30" aria-hidden="true"><circle cx="15" cy="15" r="14" fill="none" stroke="var(--brand-blue)" stroke-width="1.5"/><circle cx="15" cy="15" r="10" fill="var(--brand-blue)"/><circle cx="11.5" cy="13" r="1.3" fill="#fff"/><circle cx="18.5" cy="13" r="1.3" fill="#fff"/><path d="M10.5 17 Q15 22 19.5 17" fill="none" stroke="#fff" stroke-width="1.5" stroke-linecap="round"/></svg>
      <div><p class="benefit-title"><span class="accent">Hassle</span> <span class="muted">Free</span></p><p class="benefit-text">You're busy running a business; let us negotiate for you and put money back in your pocket!</p></div>
    </div>
    <div class="benefit" style="top:378px">
      <svg width="30" height="30" viewBox="0 0 30 30" aria-hidden="true"><circle cx="15" cy="15" r="14" fill="none" stroke="var(--brand-blue)" stroke-width="1.5"/><circle cx="15" cy="11" r="4.5" fill="var(--brand-blue)"/><text x="15" y="13.2" font-size="6" fill="#fff" text-anchor="middle" font-family="Open Sans, sans-serif" font-weight="700">$</text><path d="M6 19 H11 L15 21 H22 Q24 21 22 23 L15 24 H6 Z" fill="var(--brand-blue)"/></svg>
      <div><p class="benefit-title"><span class="accent">Save</span> <span class="muted">Money</span></p><p class="benefit-text">We save business owners an average of $500 per month</p></div>
    </div>
    <div class="benefit" style="top:448px">
      <svg width="30" height="30" viewBox="0 0 30 30" aria-hidden="true"><circle cx="15" cy="15" r="14" fill="none" stroke="var(--brand-blue)" stroke-width="1.5"/><circle cx="11" cy="9" r="2.2" fill="var(--brand-blue)"/><path d="M8 12 H14 V23 H12 V18 H10 V23 H8 Z" fill="var(--brand-blue)"/><path d="M16 12 L22 10 L22 17 Q22 21 19 23 Q16 21 16 17 Z" fill="var(--brand-blue)"/></svg>
      <div><p class="benefit-title"><span class="accent">No Risk</span><br><span class="muted">Guarantee</span></p><p class="benefit-text">We guarantee we will lower your bill or there is no charge for our service!</p></div>
    </div>

    <p class="tab" style="left:256px;top:34px">HOW IT WORKS</p>
    <svg class="shapes" width="719" height="556" viewBox="0 0 719 556" aria-hidden="true">
      <line x1="272" y1="92" x2="272" y2="330" stroke="var(--brand-blue)" stroke-width="1" stroke-dasharray="3 3"/>
      <circle cx="272" cy="332" r="3" fill="var(--brand-blue)"/>
    </svg>
    <div class="step" style="top:68px">
      <svg width="28" height="28" viewBox="0 0 28 28" aria-hidden="true"><circle cx="14" cy="14" r="14" fill="var(--brand-blue)"/><circle cx="16" cy="11" r="3" fill="none" stroke="#fff" stroke-width="1.3"/><path d="M11 20 Q16 14 21 20" fill="none" stroke="#fff" stroke-width="1.3"/><path d="M6 12 H11 M8.5 9.5 V14.5" stroke="#fff" stroke-width="1.3"/></svg>
      <div><p class="step-title">Sign Up</p><p class="step-text">Provide some basic information and a copy of your most recent statement or invoice</p></div>
    </div>
    <div class="step" style="top:152px">
      <svg width="28" height="28" viewBox="0 0 28 28" aria-hidden="true"><circle cx="14" cy="14" r="14" fill="var(--brand-blue)"/><circle cx="14" cy="10" r="3.5" fill="none" stroke="#fff" stroke-width="1.3"/><path d="M13 13.5 V15 H15 V13.5" stroke="#fff" stroke-width="1"/><path d="M6 18 H10 L13 19.5 H19 Q21 19.5 19 21 L13 22 H6" fill="none" stroke="#fff" stroke-width="1.3"/></svg>
      <div><p class="step-title">We Contact<br>Your Provider</p><p class="step-text">Our experts get to work negotiating with your current provider on your behalf for the lowest rates possible</p></div>
    </div>
    <div class="step" style="top:250px">
      <svg width="28" height="28" viewBox="0 0 28 28" aria-hidden="true"><circle cx="14" cy="14" r="14" fill="var(--brand-blue)"/><path d="M7 13 Q14 5 21 13 Z" fill="none" stroke="#fff" stroke-width="1.3"/><line x1="14" y1="13" x2="14" y2="18" stroke="#fff" stroke-width="1.2"/><circle cx="11" cy="20" r="2.3" fill="none" stroke="#fff" stroke-width="1.1"/><circle cx="17" cy="20" r="2.3" fill="none" stroke="#fff" stroke-width="1.1"/></svg>
      <div><p class="step-title">You Save<br>Money</p><p class="step-text">Your monthly fee's get reduced and you save money! We split the savings for the first year and the rest goes into your wallet. Simple!</p></div>
    </div>

    <p class="tab tab--white" style="left:490px;top:14px;width:215px">FAQ</p>
    <div class="faq">
      <p class="faq-q">How does it work?</p>
      <p class="faq-a">It's easy! Enroll in the service and send a copy of your bill or your login details. We do the rest: our experts negotiate with your provider and report back within 2-3 business days.</p>
      <p class="faq-q">How will I receive my savings?</p>
      <p class="faq-a">Your provider applies the new rates on your next billing cycle. In some cases we can even get the lower rates applied back to the start of the month.</p>
      <p class="faq-q">Will you switch my service provider without asking?</p>
      <p class="faq-a">No. We will never switch your service provider. Our goal is to save you as much money as possible while keeping you with your current provider.</p>
      <p class="faq-q">How much does Tallowbrook Ledger cost?</p>
      <p class="faq-a">Our fee is 50% of your savings for the first 12 months, earned only when we save you money. If we cannot lower your rates, there is no charge at all.</p>
      <p class="faq-q">Are there any risks involved?</p>
      <p class="faq-a">No. There are no risks and there are also no fees if we cannot save you money.</p>
    </div>
  </section>

</div>
</body>
</html>
```